Start-up Dog Daycare Needs a Retractable Banner Design for Career Fair

We are a dog daycare located in San Francisco, California, called TailNest Dog Daycare. Our small but dog-knowledgeable team gets to interact with and care for dogs on a daily basis where we supervise playgroups of various sizes. We will like a modern yet fun banner to attract potential new hires and interns. We will like the final design to communicate that we are seeking people who love dogs but who are also hard workers that can thrive in a team setting.

The product specs are as follows:
Document Trim Size - 33.13 X 86.18 inches (84.1 X 218.9cm) with 3312 X 8618 pixels.
Full Bleed Size - 33.38 X 86.43 inches (84.8 X 219.5cm) with 3338 X 8643 pixels.

Additionally, to get a better idea of our brand, attached will be our Company Brand Identity.
Furthermore, attached will be the text we will like included onto our banner.

Target Market(s)

Students at a University

Industry/Entity Type

Pet Care

Font styles to use
Sans Serif

Colors
33a6d7
fbee3e

Requirements
Must have
• Our company logo must be incorporated onto our banner.
• Please include the text in the following order:
• 1. "Dog lovers come talk to us"
• 2. "Internships and full-time positions available"
• Banner Size Specifications:
• Full Bleed Size
• 33.38" x 86.43"
• 84.8 x 219.5 cm
• 3338 x 8643 pixels
• Document Trim Size
• 33.13" x 86.18"
• 84.1 x 218.9 cm
• 3312 x 8618 pixels
• Finished artwork should extend to fill the full bleed area to avoid white edges around.
Nice to have
• - Colors Blue and Yellow
• - Image(s) of a dog(s) playing

```html
<!DOCTYPE html>
<html lang="en">
<head>
<meta charset="UTF-8">
<title>TailNest Dog Daycare – Career Fair Banner</title>
<link href="https://fonts.googleapis.com/css2?family=Baloo+2:wght@600;700;800&family=Montserrat:wght@600&display=swap" rel="stylesheet">
<style>
  :root {
    --stage: #000000;
    --sky: #86c9e8;
    --brand-blue: #2ea4da;
    --brand-yellow: #fbee3e;
    --shade-yellow: #d9cc17;
    --ink: #1d1d1b;
    --white: #ffffff;
  }
  * { margin: 0; padding: 0; box-sizing: border-box; }
  html, body {
    width: 1200px; height: 1200px; overflow: hidden;
    background: var(--stage);
  }
  .banner {
    position: absolute; left: 368px; top: 0;
    width: 464px; height: 1200px;
    background: var(--sky);
    overflow: hidden;
    font-family: "Baloo 2", sans-serif;
    text-align: center;
  }
  .banner__shapes { position: absolute; inset: 0; }
  .brand {
    position: absolute; top: 118px; left: 0; width: 100%;
    display: flex; flex-direction: column; align-items: center;
  }
  .brand__row { display: flex; align-items: center; gap: 10px; }
  .brand__dot {
    width: 14px; height: 14px; border-radius: 50%;
    background: var(--brand-yellow);
  }
  .brand__name {
    font-weight: 800; font-size: 46px; line-height: 1;
    color: var(--brand-yellow);
  }
  .brand__tagline {
    margin-top: 10px;
    font-family: "Montserrat", sans-serif; font-weight: 600;
    font-size: 12px; letter-spacing: 2.4px; color: var(--ink);
  }
  .headline {
    position: absolute; top: 218px; left: 0; width: 100%;
    color: var(--white);
  }
  .headline__main { font-weight: 800; font-size: 58px; line-height: 62px; }
  .headline__sub { font-weight: 800; font-size: 36px; line-height: 42px; }
  .offer {
    position: absolute; top: 844px; left: 0; width: 100%;
    color: var(--brand-blue);
    font-weight: 800; font-size: 40px; line-height: 48px;
  }
</style>
</head>
<body>
  <div class="banner">
    <svg class="banner__shapes" width="464" height="1200" viewBox="0 0 464 1200">
      <defs>
        <radialGradient id="dogPhotoTone" cx="50%" cy="45%" r="55%">
          <stop offset="0%" stop-color="#dfe9ee"/>
          <stop offset="55%" stop-color="#8aa7b4"/>
          <stop offset="100%" stop-color="#86c9e8" stop-opacity="0"/>
        </radialGradient>
      </defs>
      <rect class="dog-photo" x="50" y="420" width="370" height="400" rx="180"
            fill="url(#dogPhotoTone)" role="img"
            aria-label="Photo of a happy fluffy puppy with its tongue out"/>
      <path class="wave wave--shade" d="M232 756 C320 730 400 712 464 696 L464 836 C400 800 320 770 232 756 Z" fill="var(--shade-yellow)"/>
      <path class="wave wave--main" d="M0 718 C160 740 330 770 464 836 L464 1200 L0 1200 Z" fill="var(--brand-yellow)"/>
    </svg>

    <div class="brand">
      <div class="brand__row">
        <span class="brand__dot"></span>
        <span class="brand__name">TailNest</span>
      </div>
      <div class="brand__tagline">DOG DAYCARE</div>
    </div>

    <h1 class="headline">
      <div class="headline__main">Dog lovers</div>
      <div class="headline__sub">come talk to us!</div>
    </h1>

    <p class="offer">Internships<br>and full-time<br>positions<br>available!</p>
  </div>
</body>
</html>
```